Business Card Design

Contact Information for Business Card

A vertical business card request- a medium & light gray with silverfern tree logo (logo is attached)

Please use Trebuchet font -- if possible- can we use two different color gray? (See pictures attached below)
Info on the front should be the Silverfern tree logo - on the top of the card, followed by the info ...
Card to read: " " indicated what should be on the card --
Name: " Joan Pelley "
Title : "Partner "
" Office: 202.555.0147 "
" Mobile: 202.555.0182 "

Backside of the card - solid medium color gray color w/ address and small message centered in the card - Trebuchet font
to read:

" 317 B North Linden Avenue, NE "
" Washington, DC 20099 "

Then below address to read:
" Fundraising | Event Planning | Political Consulting "

```html
<!DOCTYPE html>
<html lang="en">
<head>
<meta charset="utf-8">
<title>Keston Park Group – Business Card</title>
<link rel="stylesheet" href="https://fonts.googleapis.com/css2?family=PT+Sans:wght@400;700&display=swap">
<style>
  :root {
    --page: #ffffff;
    --charcoal: #3f3f3f;
    --mid-gray: #b3b3b3;
    --tree-faint: #bdbdbd;
    --ink: #000000;
    --white: #ffffff;
    --tree-mark: #e6e6e6;
  }
  html, body {
    margin: 0;
    width: 1200px;
    height: 1000px;
    overflow: hidden;
    background: var(--page);
    font-family: "PT Sans", "Trebuchet MS", sans-serif;
  }
  .canvas { position: relative; width: 1200px; height: 1000px; }
  .card {
    position: absolute;
    top: 87px;
    width: 474px;
    height: 810px;
    background: var(--mid-gray);
    overflow: hidden;
  }
  .card--front { left: 109px; }
  .card--back { left: 617px; }

  .front__brand-panel {
    position: absolute; left: 0; top: 0;
    width: 474px; height: 435px;
    background: var(--charcoal);
  }
  .brand__tree {
    position: absolute; left: 168px; top: 72px;
    width: 242px; height: 250px;
  }
  .brand__name {
    position: absolute; left: 39px; top: 350px;
    margin: 0;
    color: var(--white);
    font-size: 38px;
    font-weight: 400;
    line-height: 1;
    letter-spacing: 0.5px;
  }

  .contact { position: absolute; left: 39px; top: 521px; color: var(--ink); }
  .contact__name { margin: 0; font-size: 27px; font-weight: 700; line-height: 32px; }
  .contact__title { margin: 0; font-size: 18px; line-height: 20px; }
  .contact__lines { margin: 30px 0 0; font-size: 25px; line-height: 30px; letter-spacing: 0.3px; }
  .contact__lines span { display: block; }

  .back__tree {
    position: absolute; left: 48px; top: 43px;
    width: 382px; height: 452px;
  }
  .back__address {
    position: absolute; left: 0; right: 0; top: 564px;
    margin: 0; text-align: center;
    color: var(--white); font-weight: 700;
    font-size: 19px; line-height: 22.5px;
    font-style: normal;
    letter-spacing: 0.3px;
  }
  .back__services {
    position: absolute; left: 0; right: 0; top: 749px;
    margin: 0; text-align: center;
    color: var(--white); font-weight: 700; font-size: 17px;
    letter-spacing: 0.3px;
  }
</style>
</head>
<body>
<main class="canvas">
  <section class="card card--front">
    <div class="front__brand-panel">
      <svg class="brand__tree" viewBox="0 0 242 250" role="img" aria-label="Bare tree illustration of the brand">
        <rect width="242" height="250" fill="var(--tree-mark)" opacity="0.25"/>
      </svg>
      <h1 class="brand__name">Keston Park Group</h1>
    </div>
    <div class="contact">
      <p class="contact__name">Joan Pelley</p>
      <p class="contact__title">Partner</p>
      <p class="contact__lines">
        <span>joan@kestonpark.com</span>
        <span>202.555.0182 mobile</span>
        <span>202.555.0147 office</span>
      </p>
    </div>
  </section>

  <section class="card card--back">
    <svg class="back__tree" viewBox="0 0 382 452" role="img" aria-label="Faint bare tree illustration in the background">
      <rect width="382" height="452" fill="var(--tree-faint)" opacity="0.5"/>
    </svg>
    <address class="back__address">
      317 North Linden Avenue, NE<br>
      Suite B<br>
      Washington, DC 20099
    </address>
    <p class="back__services">Fundraising | Event Planning | Political Consulting</p>
  </section>
</main>
</body>
</html>
```